Website Layout for Upcoming Crowdfunding ICO - Digital Currency

We need our website redesigned in a responsive format. Must be attractive with countdown timer to launch, video embedded, PDF whitepaper link, roadmap, team section and contact form. Current website on www.valdrexo.io Experience in previous ICO website designs a plus

Websites that stand out
https://lumivertoken.com/
https://greyfinchledger.com/
http://ico.vantoquelix.com/
https://www.tokvaro.io/

Target Market(s)

Bitcoin Investors
Traders
Forex traders
Ethereum Traders
ICO investors

Industry/Entity Type

Digital

Coding

Coded - Design and coding required

Number of Pages Required

1 page

Font styles to use
Sans Serif

Colors

Designer to choose colors to be used in the design.

Requirements
Must have
• countdown timer to launch, video embedded, PDF whitepaper link, roadmap, team section and contact form sections
Should not have
• Soft colors

```html
<!DOCTYPE html>
<html lang="en">
<head>
<meta charset="utf-8">
<title>Valdrexo – Asset Backed Property on the Blockchain</title>
<link rel="stylesheet" href="https://fonts.googleapis.com/css2?family=Montserrat:wght@300;400;500;600;700&family=Open+Sans:wght@400;600&display=swap">
<style>
:root{
  --blue:#4f57e8;
  --blue-deep:#3c45d6;
  --blue-soft:#6d74ee;
  --gold:#e2b22a;
  --gold-dark:#c99a16;
  --ink:#2b2b2b;
  --grey:#6f6f6f;
  --grey-light:#f3f3f3;
  --white:#ffffff;
  --video:#3a3a3a;
}
*{margin:0;padding:0;box-sizing:border-box}
html,body{width:1200px;height:2250px;overflow:hidden}
body{font-family:"Montserrat",Arial,sans-serif;color:var(--ink);background:var(--white);position:relative}
.abs{position:absolute}
.center{text-align:center;left:0;width:1200px}
.gold{color:var(--gold)}

/* hero */
.hero{position:absolute;left:0;top:0;width:1200px;height:450px;background:linear-gradient(160deg,#5a62ee 0%,#4a52e4 45%,#3f48d8 100%);color:var(--white)}
.hero-city{position:absolute;left:0;top:0;width:1200px;height:450px;background:linear-gradient(180deg,rgba(255,255,255,0.05) 0%,rgba(20,24,120,0.18) 100%)}
.brand{position:absolute;left:120px;top:36px;display:flex;flex-direction:column;align-items:center;width:90px}
.brand-mark{width:40px;height:40px;border-radius:50%;background:var(--gold)}
.brand-name{margin-top:10px;font-size:11px;font-weight:600;letter-spacing:1px;color:var(--white)}
.nav{position:absolute;top:52px;left:361px;display:flex;gap:24px;font-size:15px;font-weight:500}
.nav a{color:var(--white);text-decoration:none;padding-bottom:6px}
.nav a.active{border-bottom:2px solid var(--gold)}
.hero-title{top:186px;font-size:29px;font-weight:700;letter-spacing:.5px}
.slide-arrow{position:absolute;top:238px;width:20px;height:24px}
.count-title{top:250px;font-size:20px;font-weight:700;color:#d9d3b0}
.count-sub{top:281px;font-size:13px;font-weight:600}
.counter{position:absolute;top:346px;width:120px;text-align:center}
.counter .num{font-size:44px;font-weight:400;line-height:48px}
.counter .lbl{font-size:15px;font-weight:500}
.divider{position:absolute;top:358px;height:48px;border-left:2px dashed rgba(255,255,255,.7)}

/* business model */
.model{position:absolute;left:0;top:450px;width:1200px;height:370px;background:var(--grey-light)}
.section-title{font-size:18px;font-weight:500;color:var(--ink)}
.section-title .tag{color:var(--gold);border:1.5px solid var(--gold);padding:2px 3px}
.model-intro{top:53px;left:220px;width:780px;text-align:center;font-family:"Open Sans",Arial,sans-serif;font-size:17px;line-height:22px;color:var(--grey);font-weight:600}
.feature{position:absolute;width:330px;height:100px}
.feature-icon{position:absolute;left:0;top:0;width:68px;height:68px;border:2.5px solid var(--gold);border-radius:50%;background:var(--white);display:flex;align-items:center;justify-content:center}
.feature h3{position:absolute;left:88px;top:0;font-size:14px;font-weight:700;color:#3d3d3d}
.feature p{position:absolute;left:88px;top:25px;width:225px;font-family:"Open Sans",Arial,sans-serif;font-size:14px;line-height:22px;color:var(--grey);font-weight:600}

/* explained */
.explained{position:absolute;left:0;top:820px;width:1200px;height:370px;background:var(--white)}
.video{position:absolute;top:73px;width:458px;height:255px;background:radial-gradient(ellipse at 50% 40%,#6a6a6a 0%,#3e3e3e 70%,#303030 100%)}
.play{position:absolute;left:199px;top:92px;width:60px;height:60px;border-radius:50%;background:#d8d8d8;opacity:.9}
.video-bar{position:absolute;left:0;bottom:0;width:458px;height:30px;background:#262626}

/* invest */
.invest{position:absolute;left:0;top:1190px;width:1200px;height:350px;background:linear-gradient(90deg,#f6f6f6 0%,#eeeff3 55%,#e4e6ee 100%)}
.invest h2{font-size:18px;font-weight:600;color:var(--gold)}
.invest h4{font-size:14px;font-weight:700;color:#2f2f2f}
.invest .para{font-family:"Open Sans",Arial,sans-serif;font-size:15px;line-height:22px;color:#4a4a4a;text-indent:50px;width:410px}
.step{position:absolute;left:597px;width:500px}
.step svg{position:absolute;left:0;top:0}
.step h5{position:absolute;left:45px;top:0;font-size:14px;font-weight:700;color:#2f2f2f}
.step p{position:absolute;left:45px;top:22px;width:445px;font-family:"Open Sans",Arial,sans-serif;font-size:13.5px;line-height:18px;color:#555}

/* whitepaper */
.whitepaper{position:absolute;left:0;top:1540px;width:1200px;height:160px;background:linear-gradient(160deg,#5a62ee 0%,#4750e2 100%);color:var(--white)}
.btn{position:absolute;left:453px;top:92px;width:315px;height:48px;background:var(--gold);color:#2d2d6e;font-size:15px;font-weight:600;display:flex;align-items:center;justify-content:center;border-radius:2px}

/* roadmap */
.roadmap{position:absolute;left:0;top:1700px;width:1200px;height:235px;background:var(--white)}
.tip{position:absolute;left:102px;top:15px;width:183px;height:86px;background:var(--gold);border-radius:6px;font-size:11px;font-weight:600;line-height:14px;text-align:center;padding:7px 8px;color:#2a2a2a}
.tip:after{content:"";position:absolute;left:84px;bottom:-9px;border-left:8px solid transparent;border-right:8px solid transparent;border-top:9px solid var(--gold)}
.timeline{position:absolute;left:189px;top:133px;width:810px;height:2px;background:#d6d6d6}
.node{position:absolute;top:105px;width:57px;height:57px;border-radius:50%;border:2px solid #d0d0d0;background:var(--white);display:flex;align-items:center;justify-content:center}
.node.first{border-color:var(--gold)}
.milestone{position:absolute;top:180px;width:200px;text-align:center;font-size:12px;font-weight:600;line-height:17px;color:#2b2b2b}

/* team */
.team{position:absolute;left:0;top:1935px;width:1200px;height:315px;background:linear-gradient(160deg,#6a71ea 0%,#4f57e2 60%,#4149d4 100%);color:var(--white)}
.member{position:absolute;top:98px;width:240px;text-align:center}
.portrait{width:140px;height:140px;margin:0 auto;border-radius:50%;border:3px solid var(--gold);background:radial-gradient(circle at 50% 40%,#9a8d86 0%,#6b625f 60%,#3c3b45 100%)}
.member .name{margin-top:24px;font-size:15px;font-weight:700;line-height:18px}
.member .role{font-size:15px;font-weight:700;line-height:18px}
</style>
</head>
<body>

<header class="hero">
  <div class="hero-city" role="img" aria-label="City skyline with skyscrapers under a blue tint"></div>
  <div class="brand"><span class="brand-mark"></span><span class="brand-name">VALDREXO</span></div>
  <nav class="nav">
    <a class="active">VIDEO</a><a>CROWDSALE</a><a>JOIN OUR ICO</a><a>WHITEPAPER</a><a>ABOUT</a><a>TEAM</a><a>FAQ</a><a>CONTACT</a>
  </nav>
  <svg class="slide-arrow" style="left:88px" viewBox="0 0 20 24"><path d="M14 3 5 12l9 9" fill="none" stroke="#fff" stroke-width="3"/></svg>
  <svg class="slide-arrow" style="left:1092px" viewBox="0 0 20 24"><path d="M6 3l9 9-9 9" fill="none" stroke="#fff" stroke-width="3"/></svg>
  <h1 class="abs center hero-title">ASSET BACKED PROPERTY ON THE <span class="gold">BLOCKCHAIN</span></h1>
  <p class="abs center count-title">COUNTDOWN TO <span class="gold">CROWDSALE</span></p>
  <p class="abs center count-sub">CROWDSALE STARTS 20 NOVEMBER 2017</p>
  <div class="counter" style="left:252px"><div class="num">45</div><div class="lbl">Days</div></div>
  <div class="divider" style="left:400px"></div>
  <div class="counter" style="left:447px"><div class="num">13</div><div class="lbl">Hours</div></div>
  <div class="divider" style="left:610px"></div>
  <div class="counter" style="left:642px"><div class="num">43</div><div class="lbl">Minutes</div></div>
  <div class="divider" style="left:820px"></div>
  <div class="counter" style="left:867px"><div class="num">49</div><div class="lbl">Seconds</div></div>
</header>

<section class="model">
  <h2 class="abs center section-title" style="top:17px"><span class="tag">OUR BUSINESS</span> MODEL</h2>
  <p class="abs model-intro">Our clear cut business model on how we're provinding value for investors and plans to continue add value to the token long after the crowdsale closes.</p>

  <div class="feature" style="left:117px;top:122px">
    <div class="feature-icon"><svg width="34" height="24" viewBox="0 0 34 24"><rect x="2" y="3" width="30" height="18" fill="var(--gold)"/><rect x="6" y="7" width="22" height="10" fill="#fff"/><circle cx="17" cy="12" r="3.5" fill="var(--gold)"/></svg></div>
    <h3>RISE FUNDS</h3>
    <p>Our crowdsale will aim to raise $50 Million over a period of 4 weeks and 1 day.</p>
  </div>
  <div class="feature" style="left:450px;top:122px">
    <div class="feature-icon"><svg width="40" height="30" viewBox="0 0 40 30"><g fill="var(--gold)"><circle cx="8" cy="8" r="4"/><circle cx="20" cy="6" r="4.5"/><circle cx="32" cy="8" r="4"/><rect x="3" y="14" width="10" height="14" rx="2"/><rect x="15" y="12" width="10" height="16" rx="2"/><rect x="27" y="14" width="10" height="14" rx="2"/></g></svg></div>
    <h3>SETUP OUR TEAM</h3>
    <p>Using the funds raised and the percentages allocated we setup our team to get the ball rolling.</p>
  </div>
  <div class="feature" style="left:783px;top:122px">
    <div class="feature-icon"><svg width="36" height="32" viewBox="0 0 36 32"><path d="M8 14 20 4l12 10v10H8z" fill="var(--gold)"/><path d="M2 28h14l8-4" fill="none" stroke="var(--gold)" stroke-width="3"/></svg></div>
    <h3>BUY PROPERTY</h3>
    <p>Our team will search for good property investments and carry out due diligence.</p>
  </div>

  <div class="feature" style="left:117px;top:260px">
    <div class="feature-icon"><svg width="36" height="32" viewBox="0 0 36 32"><circle cx="11" cy="8" r="5" fill="var(--gold)"/><path d="M2 30c0-9 4-13 9-13s9 4 9 13z" fill="var(--gold)"/><rect x="20" y="10" width="14" height="11" fill="none" stroke="var(--gold)" stroke-width="2.5"/></svg></div>
    <h3>DEVELOP INVESTOR PLATFORM</h3>
    <p>Our crowdsale will aim to raise $50 Million over a period of 4 weeks and 1 day.</p>
  </div>
  <div class="feature" style="left:450px;top:260px">
    <div class="feature-icon"><svg width="36" height="32" viewBox="0 0 36 32"><g fill="var(--gold)"><ellipse cx="18" cy="6" rx="9" ry="3.5"/><ellipse cx="18" cy="12" rx="9" ry="3.5"/><ellipse cx="18" cy="18" rx="9" ry="3.5"/><rect x="2" y="24" width="32" height="5" rx="2"/></g></svg></div>
    <h3 style="font-size:13px">FUNDS ADMINISTRATION SYSTEM</h3>
    <p>Using the funds raised and the percentages allocated we setup our team to get the ball rolling.</p>
  </div>
  <div class="feature" style="left:783px;top:260px">
    <div class="feature-icon"><svg width="36" height="32" viewBox="0 0 36 32"><path d="M4 26 14 16l6 6L32 8" fill="none" stroke="var(--gold)" stroke-width="4"/><path d="M24 6h10v10" fill="none" stroke="var(--gold)" stroke-width="4"/></svg></div>
    <h3>TRADING ON THE EXCHANGES</h3>
    <p>Our team will search for good property investments and carry out due diligence.</p>
  </div>
</section>

<section class="explained">
  <h2 class="abs center section-title" style="top:24px"><span class="tag">VALDREXO</span> EXPLAINED</h2>
  <div class="video" style="left:114px" role="img" aria-label="Embedded explainer video player">
    <svg class="play" viewBox="0 0 60 60"><circle cx="30" cy="30" r="30" fill="#d8d8d8"/><path d="M23 17v26l21-13z" fill="#3a3a3a"/></svg>
    <svg class="video-bar" viewBox="0 0 458 30"><path d="M12 10v10l8-5z" fill="#ddd"/><rect x="38" y="12" width="300" height="6" rx="3" fill="#555"/><path d="M367 12h4l5-4v14l-5-4h-4z" fill="#ddd"/><rect x="390" y="12" width="55" height="6" rx="3" fill="#555"/></svg>
  </div>
  <div class="video" style="left:630px" role="img" aria-label="Embedded explainer video player">
    <svg class="play" viewBox="0 0 60 60"><circle cx="30" cy="30" r="30" fill="#d8d8d8"/><path d="M23 17v26l21-13z" fill="#3a3a3a"/></svg>
    <svg class="video-bar" viewBox="0 0 458 30"><path d="M12 10v10l8-5z" fill="#ddd"/><rect x="38" y="12" width="300" height="6" rx="3" fill="#555"/><path d="M367 12h4l5-4v14l-5-4h-4z" fill="#ddd"/><rect x="390" y="12" width="55" height="6" rx="3" fill="#555"/></svg>
  </div>
</section>

<section class="invest" role="img" aria-label="Faint office tower photograph behind investment information">
  <h2 class="abs" style="left:117px;top:24px">WHY INVEST IN OUR ICO?</h2>
  <h4 class="abs" style="left:120px;top:58px">TANGIBLE ASSET BACKING THE COIN</h4>
  <p class="abs para" style="left:117px;top:81px">Property provides good annual returns of between 8 - 10% depending on jurisdiction. Property is relatively stable unlike the share market with the risks of major fluctuations in value. The capital investment appreciates over the long run and does so consistently.</p>
  <h4 class="abs" style="left:117px;top:199px">COIN VALUE IS IMPORTANT TO US</h4>
  <p class="abs para" style="left:117px;top:220px">The general trend with CryptoCurrency coins is that the cheaper they are the more volatile they are. We have engineered a way for the coin to only be volatile in a bullish market where investors can see big profits and benefit from the company behind the coin.</p>

  <h2 class="abs" style="left:597px;top:24px">HOW DO I PARTICIPATE?</h2>
  <h4 class="abs" style="left:597px;top:48px;font-size:13px">HOW TO INVEST IN THE VALDREXO INITIAL COIN OFFERING (ICO)</h4>
  <div class="step" style="top:76px">
    <svg width="34" height="32" viewBox="0 0 34 32"><path d="M2 10h30l-4 20H6z" fill="var(--gold)"/><path d="M10 10 17 2l7 8" fill="none" stroke="var(--gold)" stroke-width="3"/></svg>
    <h5>BUY ETHER</h5>
    <p>Signup for a Cryptocurrency Wallet account and download the app if you're using a mobile phone. Buy Ether in your currency from the wallet website or app</p>
  </div>
  <div class="step" style="top:166px">
    <svg width="36" height="32" viewBox="0 0 36 32"><path d="M4 10h22l-6-6M32 22H10l6 6" fill="none" stroke="var(--gold)" stroke-width="4"/></svg>
    <h5>TRANSFER ETHER</h5>
    <p>Signup for a Cryptocurrency Wallet account and download the app if you're using a mobile phone. Buy Ether in your currency from the wallet website or app</p>
  </div>
  <div class="step" style="top:251px">
    <svg width="36" height="36" viewBox="0 0 36 36"><path d="M4 22 20 6h10v10L14 32z" fill="var(--gold)"/><circle cx="25" cy="11" r="2.5" fill="#fff"/></svg>
    <h5>RECEIVE TOKENS</h5>
    <p>Signup for a Cryptocurrency Wallet account and download the app if you're using a mobile phone. Buy Ether in your currency from the wallet website or app</p>
  </div>
</section>

<section class="whitepaper">
  <h2 class="abs center" style="top:26px;font-size:20px;font-weight:700">WHITEPAPER</h2>
  <p class="abs center" style="top:58px;font-size:14px;font-weight:600">OUR WHITEPAPER CAN BE VIEWED BELOW</p>
  <div class="btn">DOWNLOAD WHITEPAPER HERE</div>
</section>

<section class="roadmap">
  <h2 class="abs center" style="top:22px;font-size:18px;font-weight:700;color:var(--gold)">ROADMAP</h2>
  <p class="abs center" style="top:53px;font-size:15px;font-weight:500">TIMELINE OF EVENTS LEADING UP TO OUR ICO</p>
  <div class="tip">Founders create Valdrexo to raise funds to purchase properties throughout the world and create a portfolio to back the Valdrexo Token</div>
  <div class="timeline"></div>
  <div class="node first" style="left:161px"><svg width="26" height="26" viewBox="0 0 26 26"><path d="M6 3v21" stroke="var(--gold)" stroke-width="2.5"/><path d="M7 4h15l-4 5 4 5H7z" fill="var(--gold)"/></svg></div>
  <div class="node" style="left:356px"><svg width="26" height="26" viewBox="0 0 26 26"><rect x="4" y="12" width="18" height="11" fill="#8a8a8a"/><rect x="12" y="5" width="2" height="6" fill="#8a8a8a"/></svg></div>
  <div class="node" style="left:554px"><svg width="30" height="26" viewBox="0 0 30 26"><g fill="#8a8a8a"><circle cx="8" cy="8" r="3.5"/><circle cx="15" cy="6" r="4"/><circle cx="22" cy="8" r="3.5"/><rect x="3" y="13" width="24" height="9" rx="3"/></g></svg></div>
  <div class="node" style="left:762px"><svg width="28" height="28" viewBox="0 0 28 28"><circle cx="14" cy="11" r="6" fill="none" stroke="#8a8a8a" stroke-width="4" stroke-dasharray="3 2"/><path d="M3 22h14l6-4" fill="none" stroke="#8a8a8a" stroke-width="2.5"/></svg></div>
  <div class="node" style="left:971px"><svg width="30" height="24" viewBox="0 0 30 24"><path d="M2 8l8-4 6 4 6-4 6 4-8 10-6-4-6 4z" fill="#8a8a8a"/></svg></div>
  <div class="milestone" style="left:89px">JUNE 2017<br>OUR BEGINNINGS</div>
  <div class="milestone" style="left:284px">JULY 2017<br>AN ICO IS BORN</div>
  <div class="milestone" style="left:482px">NOVEMBER 2017<br>GATHER INVESTORS</div>
  <div class="milestone" style="left:690px">JANUARY 2018<br>TRANSITION TO FULL SERVICE</div>
  <div class="milestone" style="left:899px">BE PART OF OUR<br>STORY!</div>
</section>

<section class="team" role="img" aria-label="Business people walking in a bright office, blue tinted">
  <h2 class="abs center" style="top:24px;font-size:19px;font-weight:700;color:var(--gold)">OUR AMAZING TEAM</h2>
  <p class="abs center" style="top:50px;font-size:14px;font-weight:600">THE KEY PEOPLE BEHIND THE VALDREXO TOKEN AND ICO LAUNCH</p>
  <div class="member" style="left:106px"><div class="portrait" role="img" aria-label="Portrait photo of the CEO"></div><p class="name">TOMAS VERHAAL</p><p class="role">CEO, FOUNDER</p></div>
  <div class="member" style="left:345px"><div class="portrait" role="img" aria-label="Portrait photo of the CMO"></div><p class="name">DORIAN LESTRANGE</p><p class="role">CMO, CO-FOUNDER</p></div>
  <div class="member" style="left:585px"><div class="portrait" role="img" aria-label="Portrait photo of the CTO"></div><p class="name">RAVI CASTELLAN</p><p class="role">CTO, CO-FOUNDER</p></div>
  <div class="member" style="left:825px"><div class="portrait" role="img" aria-label="Portrait photo of the social media manager"></div><p class="name">JALEN MOORCROFT</p><p class="role">SOCIAL MEDIA MANAGER</p></div>
</section>

</body>
</html>
```